Turn this into a clear and concise

Attached is a screen shot that we currently show to investors from a software program. We need you to illustrate this in a much more professional looking and easy to view and understand way. If we like your style and attention to detail there is more work behind this.
Industry/Entity Type
Software

```html
<!DOCTYPE html>
<html lang="en">
<head>
<meta charset="utf-8">
<title>Intra-day Countertrend US Hours</title>
<link rel="stylesheet" href="https://fonts.googleapis.com/css2?family=Source+Sans+3:wght@400;600;700&display=swap">
<style>
  :root{
    --ink:#3a5570;
    --frame:#4b6278;
    --axis:#3e3e3e;
    --plot:#ffffff;
    --grid:#2b2b2b;
    --session:#d6dce3;
    --green:#8dc63f;
    --candle-up:#b9e69d;
    --candle-down:#d11f2a;
    --candle-edge:#3d3d3d;
    --level:#f5a623;
    --pivot:#3a55a0;
    --limit:#d11f2a;
    --divider:#6fd0d2;
    --osc-high:#f4a58c;
    --osc-low:#6b2fa0;
    --volume:#2b4a9e;
    --label:#ffffff;
  }
  html,body{margin:0;padding:0;width:1200px;height:725px;overflow:hidden;background:#fff;}
  .board{display:block;width:1200px;height:725px;font-family:"Source Sans 3",sans-serif;}
  .title{fill:var(--ink);font-weight:700;font-size:13.5px;text-anchor:middle;}
  .panel-label{fill:var(--green);font-weight:700;font-size:11px;text-anchor:middle;}
  .frame{fill:var(--frame);}
  .plot{fill:var(--plot);}
  .axis{fill:var(--axis);}
  .session{fill:var(--session);}
  .grid{stroke:var(--grid);stroke-width:.6;}
  .divider{stroke:var(--divider);stroke-width:1;}
  .limit{stroke:var(--limit);stroke-width:1.2;}
  .level{stroke:var(--level);stroke-width:1;stroke-dasharray:3 2;}
  .pivot{stroke:var(--pivot);stroke-width:1;stroke-dasharray:3 2;}
  .osc-high{stroke:var(--osc-high);stroke-width:1.4;}
  .osc-low{stroke:var(--osc-low);stroke-width:1.2;}
  .osc{fill:none;stroke:var(--green);stroke-width:2.6;stroke-linejoin:round;}
  .wick{stroke:var(--candle-edge);stroke-width:.8;}
  .up{fill:var(--candle-up);stroke:var(--candle-edge);stroke-width:.5;}
  .down{fill:var(--candle-down);stroke:#8a1218;stroke-width:.5;}
  .vol rect{fill:var(--volume);}
  .time-band{fill:var(--green);}
  .time{fill:#1e1e1e;font-weight:700;font-size:12px;text-anchor:middle;}
  .price{fill:var(--label);font-weight:700;font-size:13px;}
  .price-sm{fill:var(--label);font-weight:600;font-size:7px;}
  .signal{fill:var(--candle-down);stroke:#7a0f14;stroke-width:.5;}
</style>
</head>
<body>
<svg class="board" viewBox="0 0 900 544" xmlns="http://www.w3.org/2000/svg" role="img" aria-label="Entry and exit example for an intra-day countertrend trade">
  <text class="title" x="450" y="47">Intra-day Countertrend US Hours</text>
  <text class="title" x="450" y="66">Example Trade: 30 year Treasury Bond, 7/13/14 “Payroll Friday”</text>

  <!-- ENTRY PANEL -->
  <g class="chart chart-entry">
    <text class="panel-label" x="235" y="101">ENTRY (SELL)</text>
    <rect class="frame" x="48" y="107" width="373" height="390"/>
    <rect class="plot" x="62" y="118" width="274" height="342"/>
    <rect class="axis" x="336" y="118" width="72" height="342"/>
    <rect class="session" x="125" y="122" width="160" height="146"/>

    <g class="grid-lines">
      <line class="grid" x1="112" y1="118" x2="112" y2="460"/>
      <line class="grid" x1="182" y1="118" x2="182" y2="460"/>
      <line class="grid" x1="252" y1="118" x2="252" y2="460"/>
      <line class="grid" x1="318" y1="118" x2="318" y2="460"/>
      <line class="grid" x1="62" y1="195" x2="336" y2="195"/>
      <line class="grid" x1="62" y1="225" x2="336" y2="225"/>
      <line class="grid" x1="62" y1="258" x2="336" y2="258"/>
      <line class="grid" x1="62" y1="278" x2="336" y2="278"/>
      <line class="grid" x1="62" y1="368" x2="336" y2="368"/>
      <line class="grid" x1="62" y1="388" x2="336" y2="388"/>
      <line class="grid" x1="62" y1="414" x2="336" y2="414"/>
    </g>
    <line class="limit" x1="62" y1="135" x2="336" y2="135"/>
    <g class="levels">
      <line class="level" x1="62" y1="149" x2="336" y2="149"/>
      <line class="level" x1="62" y1="157" x2="336" y2="157"/>
      <line class="level" x1="62" y1="165" x2="336" y2="165"/>
      <line class="level" x1="62" y1="174" x2="336" y2="174"/>
      <line class="level" x1="62" y1="182" x2="336" y2="182"/>
    </g>
    <line class="divider" x1="62" y1="262" x2="408" y2="262"/>
    <line class="divider" x1="62" y1="378" x2="408" y2="378"/>
    <line class="osc-high" x1="62" y1="293" x2="336" y2="293"/>
    <line class="osc-low" x1="62" y1="348" x2="336" y2="348"/>

    <g class="candles">
      <line class="wick" x1="82" y1="168" x2="82" y2="180"/><rect class="down" x="79.5" y="170" width="5" height="8"/>
      <line class="wick" x1="90" y1="175" x2="90" y2="186"/><rect class="down" x="87.5" y="177" width="5" height="6"/>
      <line class="wick" x1="98" y1="177" x2="98" y2="184"/><rect class="up" x="95.5" y="179" width="5" height="3"/>
      <line class="wick" x1="106" y1="176" x2="106" y2="182"/><rect class="up" x="103.5" y="177" width="5" height="3"/>
      <line class="wick" x1="114" y1="176" x2="114" y2="184"/><rect class="down" x="111.5" y="178" width="5" height="4"/>
      <line class="wick" x1="122" y1="180" x2="122" y2="188"/><rect class="down" x="119.5" y="182" width="5" height="3"/>
      <line class="wick" x1="130" y1="183" x2="130" y2="190"/><rect class="down" x="127.5" y="185" width="5" height="3"/>
      <line class="wick" x1="138" y1="186" x2="138" y2="200"/><rect class="down" x="135.5" y="188" width="5" height="10"/>
      <line class="wick" x1="146" y1="196" x2="146" y2="214"/><rect class="down" x="143.5" y="198" width="5" height="12"/>
      <line class="wick" x1="154" y1="210" x2="154" y2="244"/><rect class="down" x="151.5" y="212" width="5" height="20"/>
      <line class="wick" x1="162" y1="230" x2="162" y2="262"/><rect class="up" x="159.5" y="232" width="5" height="10"/>
      <line class="wick" x1="170" y1="226" x2="170" y2="238"/><rect class="up" x="167.5" y="228" width="5" height="6"/>
      <line class="wick" x1="178" y1="222" x2="178" y2="232"/><rect class="up" x="175.5" y="224" width="5" height="5"/>
      <line class="wick" x1="186" y1="220" x2="186" y2="228"/><rect class="up" x="183.5" y="222" width="5" height="3"/>
      <line class="wick" x1="194" y1="217" x2="194" y2="226"/><rect class="up" x="191.5" y="219" width="5" height="4"/>
      <line class="wick" x1="202" y1="216" x2="202" y2="226"/><rect class="down" x="199.5" y="218" width="5" height="6"/>
      <line class="wick" x1="210" y1="219" x2="210" y2="227"/><rect class="up" x="207.5" y="221" width="5" height="4"/>
      <line class="wick" x1="218" y1="214" x2="218" y2="224"/><rect class="up" x="215.5" y="216" width="5" height="6"/>
      <line class="wick" x1="226" y1="212" x2="226" y2="222"/><rect class="down" x="223.5" y="215" width="5" height="5"/>
      <line class="wick" x1="234" y1="200" x2="234" y2="220"/><rect class="up" x="231.5" y="202" width="5" height="16"/>
      <line class="wick" x1="242" y1="196" x2="242" y2="206"/><rect class="up" x="239.5" y="198" width="5" height="6"/>
      <line class="wick" x1="250" y1="196" x2="250" y2="208"/><rect class="down" x="247.5" y="198" width="5" height="7"/>
      <line class="wick" x1="258" y1="203" x2="258" y2="224"/><rect class="down" x="255.5" y="205" width="5" height="9"/>
      <line class="wick" x1="266" y1="206" x2="266" y2="216"/><rect class="up" x="263.5" y="208" width="5" height="5"/>
      <line class="wick" x1="274" y1="204" x2="274" y2="212"/><rect class="up" x="271.5" y="206" width="5" height="4"/>
      <line class="wick" x1="282" y1="198" x2="282" y2="210"/><rect class="up" x="279.5" y="200" width="5" height="7"/>
      <line class="wick" x1="290" y1="188" x2="290" y2="202"/><rect class="up" x="287.5" y="190" width="5" height="10"/>
      <line class="wick" x1="298" y1="186" x2="298" y2="195"/><rect class="up" x="295.5" y="188" width="5" height="5"/>
      <line class="wick" x1="306" y1="184" x2="306" y2="193"/><rect class="up" x="303.5" y="186" width="5" height="5"/>
      <line class="wick" x1="314" y1="180" x2="314" y2="191"/><rect class="up" x="311.5" y="182" width="5" height="7"/>
      <line class="wick" x1="322" y1="172" x2="322" y2="186"/><rect class="up" x="319.5" y="175" width="5" height="8"/>
    </g>
    <path class="signal" d="M314 158 h8 v4 h3 l-7 7 l-7 -7 h3 z"/>

    <polyline class="osc" points="77,336 82,350 97,352 105,335 112,335 120,349 127,350 138,360 160,364 168,338 175,338 183,328 190,328 196,316 203,316 210,330 218,310 226,310 234,292 240,288 248,305 255,327 262,318 270,320 276,320 289,294 297,311 305,310 315,292 330,292"/>

    <g class="vol">
      <rect x="64" y="436" width="3" height="22"/><rect x="70.5" y="432" width="3" height="26"/>
      <rect x="77" y="438" width="3" height="20"/><rect x="83.5" y="448" width="3" height="10"/>
      <rect x="90" y="434" width="3" height="24"/><rect x="96.5" y="440" width="3" height="18"/>
      <rect x="103" y="444" width="3" height="14"/><rect x="109.5" y="452" width="3" height="6"/>
      <rect x="116" y="448" width="3" height="10"/><rect x="122.5" y="446" width="3" height="12"/>
      <rect x="129" y="446" width="3" height="12"/><rect x="135.5" y="440" width="3" height="18"/>
      <rect x="142" y="436" width="3" height="22"/><rect x="148.5" y="430" width="3" height="28"/>
      <rect x="155" y="383" width="3" height="75"/><rect x="161.5" y="410" width="3" height="48"/>
      <rect x="168" y="444" width="3" height="14"/><rect x="174.5" y="422" width="3" height="36"/>
      <rect x="181" y="422" width="3" height="36"/><rect x="187.5" y="450" width="3" height="8"/>
      <rect x="194" y="432" width="3" height="26"/><rect x="200.5" y="438" width="3" height="20"/>
      <rect x="207" y="446" width="3" height="12"/><rect x="213.5" y="440" width="3" height="18"/>
      <rect x="220" y="450" width="3" height="8"/><rect x="226.5" y="410" width="3" height="48"/>
      <rect x="233" y="432" width="3" height="26"/><rect x="239.5" y="436" width="3" height="22"/>
      <rect x="246" y="450" width="3" height="8"/><rect x="252.5" y="442" width="3" height="16"/>
      <rect x="259" y="446" width="3" height="12"/><rect x="265.5" y="446" width="3" height="12"/>
      <rect x="272" y="444" width="3" height="14"/><rect x="278.5" y="442" width="3" height="16"/>
      <rect x="285" y="438" width="3" height="20"/><rect x="291.5" y="434" width="3" height="24"/>
      <rect x="298" y="438" width="3" height="20"/><rect x="304.5" y="434" width="3" height="24"/>
      <rect x="311" y="444" width="3" height="14"/>
    </g>

    <g class="axis-labels">
      <text class="price" x="346" y="140">137’24</text>
      <text class="price-sm" x="346" y="152">137’20</text>
      <text class="price-sm" x="346" y="160">137’18</text>
      <text class="price-sm" x="346" y="168">137’16</text>
      <text class="price-sm" x="346" y="177">137’14</text>
      <text class="price-sm" x="346" y="185">137’12</text>
      <text class="price" x="346" y="200">137’08</text>
      <text class="price" x="346" y="230">136’28</text>
      <text class="price" x="346" y="263">136’16</text>
      <text class="price" x="346" y="283">100</text>
      <text class="price" x="350" y="373">0</text>
      <text class="price" x="346" y="393">20,000</text>
      <text class="price" x="346" y="419">10,000</text>
    </g>
    <rect class="time-band" x="62" y="460" width="346" height="30"/>
    <text class="time" x="112" y="480">8am</text>
    <text class="time" x="182" y="480">9am</text>
    <text class="time" x="252" y="480">10am</text>
    <text class="time" x="318" y="480">11am</text>
  </g>

  <!-- EXIT PANEL -->
  <g class="chart chart-exit" transform="translate(440 0)">
    <text class="panel-label" x="235" y="101">EXIT (BUY)</text>
    <rect class="frame" x="48" y="107" width="373" height="390"/>
    <rect class="plot" x="62" y="118" width="274" height="342"/>
    <rect class="axis" x="336" y="118" width="72" height="342"/>
    <rect class="session" x="125" y="122" width="160" height="146"/>

    <g class="grid-lines">
      <line class="grid" x1="112" y1="118" x2="112" y2="460"/>
      <line class="grid" x1="182" y1="118" x2="182" y2="460"/>
      <line class="grid" x1="252" y1="118" x2="252" y2="460"/>
      <line class="grid" x1="318" y1="118" x2="318" y2="460"/>
      <line class="grid" x1="62" y1="135" x2="336" y2="135"/>
      <line class="grid" x1="62" y1="195" x2="336" y2="195"/>
      <line class="grid" x1="62" y1="225" x2="336" y2="225"/>
      <line class="grid" x1="62" y1="258" x2="336" y2="258"/>
      <line class="grid" x1="62" y1="278" x2="336" y2="278"/>
      <line class="grid" x1="62" y1="368" x2="336" y2="368"/>
      <line class="grid" x1="62" y1="388" x2="336" y2="388"/>
      <line class="grid" x1="62" y1="414" x2="336" y2="414"/>
    </g>
    <line class="level" x1="62" y1="161" x2="336" y2="161"/>
    <line class="pivot" x1="62" y1="181" x2="336" y2="181"/>
    <line class="divider" x1="62" y1="267" x2="408" y2="267"/>
    <line class="divider" x1="62" y1="378" x2="408" y2="378"/>
    <line class="osc-low" x1="62" y1="348" x2="336" y2="348"/>

    <g class="candles">
      <line class="wick" x1="82" y1="167" x2="82" y2="180"/><rect class="down" x="79.5" y="169" width="5" height="9"/>
      <line class="wick" x1="90" y1="176" x2="90" y2="184"/><rect class="down" x="87.5" y="178" width="5" height="4"/>
      <line class="wick" x1="98" y1="177" x2="98" y2="183"/><rect class="up" x="95.5" y="179" width="5" height="2"/>
      <line class="wick" x1="106" y1="176" x2="106" y2="182"/><rect class="up" x="103.5" y="178" width="5" height="2"/>
      <line class="wick" x1="114" y1="176" x2="114" y2="184"/><rect class="down" x="111.5" y="178" width="5" height="4"/>
      <line class="wick" x1="122" y1="180" x2="122" y2="188"/><rect class="down" x="119.5" y="182" width="5" height="3"/>
      <line class="wick" x1="130" y1="183" x2="130" y2="192"/><rect class="down" x="127.5" y="185" width="5" height="5"/>
      <line class="wick" x1="138" y1="188" x2="138" y2="204"/><rect class="down" x="135.5" y="190" width="5" height="12"/>
      <line class="wick" x1="146" y1="200" x2="146" y2="216"/><rect class="down" x="143.5" y="202" width="5" height="10"/>
      <line class="wick" x1="154" y1="210" x2="154" y2="246"/><rect class="down" x="151.5" y="212" width="5" height="20"/>
      <line class="wick" x1="162" y1="228" x2="162" y2="262"/><rect class="up" x="159.5" y="230" width="5" height="12"/>
      <line class="wick" x1="170" y1="226" x2="170" y2="236"/><rect class="up" x="167.5" y="228" width="5" height="5"/>
      <line class="wick" x1="178" y1="222" x2="178" y2="230"/><rect class="up" x="175.5" y="224" width="5" height="4"/>
      <line class="wick" x1="186" y1="219" x2="186" y2="227"/><rect class="up" x="183.5" y="221" width="5" height="3"/>
      <line class="wick" x1="194" y1="216" x2="194" y2="225"/><rect class="up" x="191.5" y="218" width="5" height="4"/>
      <line class="wick" x1="202" y1="216" x2="202" y2="226"/><rect class="down" x="199.5" y="218" width="5" height="6"/>
      <line class="wick" x1="210" y1="216" x2="210" y2="226"/><rect class="up" x="207.5" y="218" width="5" height="5"/>
      <line class="wick" x1="218" y1="210" x2="218" y2="222"/><rect class="up" x="215.5" y="212" width="5" height="7"/>
      <line class="wick" x1="226" y1="200" x2="226" y2="216"/><rect class="up" x="223.5" y="202" width="5" height="11"/>
      <line class="wick" x1="234" y1="196" x2="234" y2="208"/><rect class="up" x="231.5" y="198" width="5" height="7"/>
      <line class="wick" x1="242" y1="196" x2="242" y2="210"/><rect class="down" x="239.5" y="198" width="5" height="8"/>
      <line class="wick" x1="250" y1="202" x2="250" y2="222"/><rect class="down" x="247.5" y="204" width="5" height="10"/>
      <line class="wick" x1="258" y1="204" x2="258" y2="216"/><rect class="up" x="255.5" y="206" width="5" height="6"/>
      <line class="wick" x1="266" y1="202" x2="266" y2="212"/><rect class="up" x="263.5" y="204" width="5" height="5"/>
      <line class="wick" x1="274" y1="196" x2="274" y2="208"/><rect class="up" x="271.5" y="198" width="5" height="7"/>
      <line class="wick" x1="282" y1="188" x2="282" y2="200"/><rect class="up" x="279.5" y="190" width="5" height="8"/>
      <line class="wick" x1="290" y1="184" x2="290" y2="194"/><rect class="up" x="287.5" y="186" width="5" height="5"/>
      <line class="wick" x1="298" y1="182" x2="298" y2="192"/><rect class="up" x="295.5" y="184" width="5" height="6"/>
      <line class="wick" x1="306" y1="182" x2="306" y2="190"/><rect class="down" x="303.5" y="184" width="5" height="4"/>
      <line class="wick" x1="314" y1="178" x2="314" y2="188"/><rect class="up" x="311.5" y="180" width="5" height="6"/>
      <line class="wick" x1="322" y1="174" x2="322" y2="183"/><rect class="up" x="319.5" y="176" width="5" height="5"/>
    </g>
    <path class="signal" d="M304 156 h8 v4 h3 l-7 7 l-7 -7 h3 z"/>

    <polyline class="osc" points="77,348 87,348 95,330 102,330 108,342 117,344 125,352 142,360 148,364 155,330 162,330 170,326 178,312 186,325 198,326 207,306 215,306 224,290 231,290 240,320 248,310 258,316 277,296 289,316 299,303 310,290 320,294 331,304"/>

    <g class="vol">
      <rect x="82" y="452" width="3" height="6"/><rect x="88" y="452" width="3" height="6"/>
      <rect x="94" y="452" width="3" height="6"/><rect x="100" y="454" width="3" height="4"/>
      <rect x="106" y="448" width="3" height="10"/><rect x="112" y="448" width="3" height="10"/>
      <rect x="118" y="446" width="3" height="12"/><rect x="124" y="448" width="3" height="10"/>
      <rect x="130" y="444" width="3" height="14"/><rect x="136" y="438" width="3" height="20"/>
      <rect x="142" y="450" width="3" height="8"/><rect x="148" y="436" width="3" height="22"/>
      <rect x="154" y="430" width="3" height="28"/><rect x="160" y="380" width="3" height="78"/>
      <rect x="166" y="408" width="3" height="50"/><rect x="172" y="394" width="3" height="64"/>
      <rect x="178" y="434" width="3" height="24"/><rect x="184" y="436" width="3" height="22"/>
      <rect x="190" y="444" width="3" height="14"/><rect x="196" y="450" width="3" height="8"/>
      <rect x="202" y="448" width="3" height="10"/><rect x="208" y="442" width="3" height="16"/>
      <rect x="214" y="432" width="3" height="26"/><rect x="220" y="442" width="3" height="16"/>
      <rect x="226" y="438" width="3" height="20"/><rect x="232" y="444" width="3" height="14"/>
      <rect x="238" y="410" width="3" height="48"/><rect x="244" y="446" width="3" height="12"/>
      <rect x="250" y="430" width="3" height="28"/><rect x="256" y="430" width="3" height="28"/>
      <rect x="262" y="432" width="3" height="26"/><rect x="268" y="438" width="3" height="20"/>
      <rect x="274" y="450" width="3" height="8"/><rect x="280" y="444" width="3" height="14"/>
      <rect x="286" y="442" width="3" height="16"/><rect x="292" y="442" width="3" height="16"/>
      <rect x="298" y="440" width="3" height="18"/><rect x="304" y="440" width="3" height="18"/>
      <rect x="310" y="414" width="3" height="44"/><rect x="316" y="424" width="3" height="34"/>
      <rect x="322" y="442" width="3" height="16"/><rect x="328" y="444" width="3" height="14"/>
    </g>

    <g class="axis-labels">
      <text class="price" x="346" y="140">137’24</text>
      <text class="price-sm" x="346" y="167">137’16</text>
      <text class="price-sm" x="346" y="183">137’10</text>
      <text class="price" x="346" y="200">137’08</text>
      <text class="price" x="346" y="230">136’28</text>
      <text class="price" x="346" y="263">136’16</text>
      <text class="price" x="346" y="283">100</text>
      <text class="price" x="350" y="373">0</text>
      <text class="price" x="346" y="393">20,000</text>
      <text class="price" x="346" y="419">10,000</text>
    </g>
    <rect class="time-band" x="62" y="460" width="346" height="30"/>
    <text class="time" x="112" y="480">8am</text>
    <text class="time" x="182" y="480">9am</text>
    <text class="time" x="252" y="480">10am</text>
    <text class="time" x="318" y="480">11am</text>
  </g>
</svg>
</body>
</html>
```